Online trading school - Website design

We are building an online trading school (trading of shares, commodities, indices, currencies). The purpose is to teach online traders how to trade successfully. We need to design the homepage of the website and logo (bramwelloq.com will be the domain). The homepage will contain the following elements

- logo
- Sign in and Register links/buttons
- upper menu
- short introduction
- a couple of bullet points 'Why to join our school?'
- sign up form
- text
- bottom menu

Attached is a draft for the designer. The draft is just for an inspiration, the actual structure of the website can be different if the designer thinks so.

The designer is free to choose colors.

School

3 page

```html
<!DOCTYPE html>
<html lang="en">
<head>
<meta charset="utf-8">
<title>bramwelloq — online trading school</title>
<link href="https://fonts.googleapis.com/css2?family=Arimo:wght@400;700&display=swap" rel="stylesheet">
<style>
:root{
  --accent:#e0592c;
  --header-bg:#d6d6d6;
  --section-bg:#ebebed;
  --footer-bg:#777777;
  --ink:#1c1c1c;
  --muted:#555555;
  --link-blue:#4a8ad0;
  --submit-blue:#2f6bb5;
  --social:#8a8f96;
}
*{box-sizing:border-box;margin:0;padding:0}
html,body{width:938px;height:1200px;overflow:hidden;background:#fff}
body{font-family:'Arimo',Arial,sans-serif;color:var(--ink);position:relative}
.site-header{position:absolute;left:0;top:6px;width:938px;height:104px;background:var(--header-bg)}
.brand{position:absolute;left:128px;top:18px;display:flex;align-items:center;gap:10px}
.brand-mark{width:52px;height:52px;border-radius:50%;background:var(--accent)}
.brand-name{font-size:34px;font-weight:700;color:var(--accent);line-height:1}
.brand-tagline{position:absolute;left:198px;top:60px;font-size:14px;font-weight:700;color:var(--ink)}
.account-links{position:absolute;top:16px;left:674px;display:flex;gap:12px}
.account-links a{display:block;height:22px;line-height:20px;padding:0 9px;border:1px solid var(--link-blue);border-radius:3px;background:#fff;color:var(--link-blue);font-size:12px;text-decoration:none}
.account-links a.register{width:73px;text-align:center}
.social{position:absolute;top:58px;left:685px;display:flex;gap:11px}
.social span{width:31px;height:31px;background:var(--social);display:block}
.main-nav{position:absolute;top:110px;left:0;width:938px;height:47px;background:#fff}
.main-nav a{position:absolute;top:12px;height:24px;line-height:24px;background:var(--accent);color:#fff;font-size:12.5px;text-align:center;text-decoration:none}
.hero{position:absolute;top:157px;left:0;width:938px;height:367px;background:linear-gradient(120deg,#c9d3de 0%,#9fb3c8 40%,#5f86b0 70%,#2c4f7e 100%)}
.intro{position:absolute;left:116px;top:159px;width:703px;height:180px;background:rgba(235,238,242,.82);border:1px solid rgba(255,255,255,.9);border-radius:6px;padding:26px 24px}
.intro h1{font-size:14.5px;font-weight:700;color:#444;margin-bottom:18px}
.intro p{font-size:13.4px;line-height:19.2px;color:var(--muted)}
.content{position:absolute;top:524px;left:0;width:938px;height:609px;background:var(--section-bg)}
.why{position:absolute;left:140px;top:28px}
.why h2{font-size:12px;font-weight:700;margin-bottom:10px}
.why ul{list-style:none}
.why li{display:flex;align-items:center;gap:8px;font-size:12px;height:21.3px;padding-left:11px}
.why svg{width:13px;height:13px}
.signup{position:absolute;left:543px;top:26px;width:260px}
.signup h2{font-size:14px;font-weight:700;margin-bottom:7px}
.signup .field{display:block;width:176px;height:24px;border:1px solid #ccc;border-radius:2px;background:#fff;font:12px 'Arimo',Arial,sans-serif;color:#999;padding:0 4px;margin-bottom:8px}
.agree{display:flex;align-items:center;gap:9px;font-size:13.5px;margin:1px 0 0 4px}
.agree span.box{width:10px;height:10px;border:1px solid #999;border-radius:2px;background:#f4f4f4}
.submit{position:absolute;left:92px;top:168px;width:85px;height:22px;background:var(--submit-blue);color:#fff;border:none;border-radius:2px;font:12px 'Arimo',Arial,sans-serif}
.offer{position:absolute;left:140px;top:248px;width:238px}
.offer h2{font-size:15px;font-weight:700;margin-bottom:18px}
.offer p{font-size:13px;line-height:18.4px}
.offer-photo{position:absolute;left:380px;top:236px;width:558px;height:373px;background:linear-gradient(90deg,#ebebed 0%,#e2e2e4 35%,#c9c3bb 60%,#e4e4e6 100%)}
.site-footer{position:absolute;top:1141px;left:0;width:938px;height:59px;background:var(--footer-bg);color:#fff;font-size:13.5px;text-align:center;line-height:59px}
</style>
</head>
<body>
<header class="site-header">
  <div class="brand"><span class="brand-mark"></span><span class="brand-name">bramwelloq</span></div>
  <div class="brand-tagline">online trading school</div>
  <div class="account-links"><a href="#">Sign in</a><a class="register" href="#">Rigester</a></div>
  <div class="social"><span aria-label="Chatterly"></span><span aria-label="Orbitly"></span><span aria-label="Peeple"></span></div>
</header>
<nav class="main-nav">
  <a href="#" style="left:130px;width:150px">About our schoo</a>
  <a href="#" style="left:284px;width:133px">Risk worning</a>
  <a href="#" style="left:421px;width:90px">FAQ</a>
  <a href="#" style="left:516px;width:154px">Trading Glossary</a>
  <a href="#" style="left:675px;width:106px">Contact</a>
</nav>
<section class="hero" role="img" aria-label="Blue toned image of molecular network, globe and connected people above a laptop">
  <div class="intro">
    <h1>Curabitur arcu erat,</h1>
    <p>accumsan id imperdiet et, porttitor at sem. Praesent sapien massa, convallis a pellentesque nec, egestas non nisi. Curabitur arcu erat, accumsan id imperdiet et, porttitor at sem. Donec rutrum congue leo eget malesuada. Pellentesque in ipsum id orci porta dapibus. Praesent sapien massa, convallis a pellentesque nec, egestas non nisi. Lorem ipsum dolor sit amet, consectetur adipiscing elit. Cras ultricies ligula sed magna dictum porta. Curabitur aliquet quam id dui posuere blandit. Curabitur aliquet quam id dui posuere blandit.</p>
  </div>
</section>
<main class="content">
  <div class="why">
    <h2>Why to Join us?</h2>
    <ul>
      <li><svg viewBox="0 0 12 12"><path d="M6 0.5 7.4 4.3 11.5 4.6 8.3 7.1 9.4 11.2 6 8.9 2.6 11.2 3.7 7.1 0.5 4.6 4.6 4.3Z" fill="none" stroke="#555" stroke-width="1"/></svg>Best trading tips ever</li>
      <li><svg viewBox="0 0 12 12"><path d="M6 0.5 7.4 4.3 11.5 4.6 8.3 7.1 9.4 11.2 6 8.9 2.6 11.2 3.7 7.1 0.5 4.6 4.6 4.3Z" fill="none" stroke="#555" stroke-width="1"/></svg>Secret tips from experts</li>
      <li><svg viewBox="0 0 12 12"><path d="M6 0.5 7.4 4.3 11.5 4.6 8.3 7.1 9.4 11.2 6 8.9 2.6 11.2 3.7 7.1 0.5 4.6 4.6 4.3Z" fill="none" stroke="#555" stroke-width="1"/></svg>We teach you how to trade online</li>
      <li><svg viewBox="0 0 12 12"><path d="M6 0.5 7.4 4.3 11.5 4.6 8.3 7.1 9.4 11.2 6 8.9 2.6 11.2 3.7 7.1 0.5 4.6 4.6 4.3Z" fill="none" stroke="#555" stroke-width="1"/></svg>Learn how to trade commodities</li>
      <li><svg viewBox="0 0 12 12"><path d="M6 0.5 7.4 4.3 11.5 4.6 8.3 7.1 9.4 11.2 6 8.9 2.6 11.2 3.7 7.1 0.5 4.6 4.6 4.3Z" fill="none" stroke="#555" stroke-width="1"/></svg>Learn how to become a trade</li>
    </ul>
  </div>
  <form class="signup">
    <h2>Join our school now!</h2>
    <span class="field" style="line-height:22px">First Name</span>
    <span class="field" style="line-height:22px">Last Name</span>
    <span class="field" style="line-height:22px">Email</span>
    <div class="agree"><span class="box"></span>Agree with our terms and Conditions</div>
    <button class="submit" type="button">Submit</button>
  </form>
  <div class="offer-photo" role="img" aria-label="Woman with ponytail writing at a white desk with plants, seen from behind"></div>
  <div class="offer">
    <h2>What do we offer?</h2>
    <p>Sed porttitor lectus nibh. Nulla porttitor accumsan tincidunt. Mauris blandit aliquet elit, eget tincidunt nibh pulvinar a. Vivamus magna justo, lacinia eget consectetur sed, convallis at tellus. Quisque velit nisi, pretium ut lacinia in, elementum id enim. Cras ultricies ligula sed magna dictum porta. Nulla porttitor accumsan tincidunt. Curabitur non nulla sit amet nisl tempus convallis quis ac lectus. Pellentesque in ipsum id orci porta dapibus. Donec rutrum congue leo eget malesuada.</p>
  </div>
</main>
<footer class="site-footer">Copyright © Your Website 2016</footer>
</body>
</html>
```